Valdarossi’s Artisan Pizzeria Menu Contest

I’m looking for a menu design for a new pizzeria - it’s farm to table type of restaurant - more upscale than a typical pizzeria - white washed wood interior with some industrial accents - I am looking for a creative menu layout using the attached sample menu items -
Valdarossi’s is an artisanal pizzeria with an atmosphere that will make you feel at home for any situation, first date, anniversary, business lunch, boys night out or girls night out with a menu inspired by the idea of a simple honest cooking paired with fresh – quality ingredients. Full service dining experience that is still casual but dedicated to extraordinary hospitality.
While developing the menu we have created a network of amazing farms and purveyors to supply our restaurant with fresh milled 100% California flour for our hand crafted dough, as well as sustainably farmed organic produce, meats and cheeses.
The menu includes classics like the Margherita pizza to daily seasonal specials, fresh salads to rustic small plates including moms meatball recipe to a fresh local burrata with handmade bread. Each dish reflects our passion for sourcing the freshest quality local ingredients.
To compliment the menu, Valdarossi’s serves an extensive wine list with selections focusing on Italian varietals. The cocktail program has been carefully crafted to offer something to entice ever palate and the beer list has unique selections of the world’s finest brewers.
Target Market(s)
25-45 year old men and women
Industry/Entity Type
American Restaurant
Requirements
Must have
- professional tone
Nice to have
- a balance of elegance and industrial (rustic)
Should not have
- photos or playful graphics etc..

```html
<!DOCTYPE html>
<html lang="en">
<head>
<meta charset="utf-8">
<title>Valdarossi’s Artisan Pizzeria Menu</title>
<link rel="stylesheet" href="https://fonts.googleapis.com/css2?family=Cinzel:wght@400;600;700&family=Crimson+Text:wght@400;600;700&display=swap">
<style>
  :root {
    --page: #ececec;
    --board: #1c1b1c;
    --accent: #c4555e;
    --ink: #ffffff;
    --ink-soft: #d8d8d8;
    --rule: #b9b9b9;
  }
  * { box-sizing: border-box; margin: 0; padding: 0; }
  html, body { width: 1200px; height: 1200px; overflow: hidden; background: var(--page); }
  .menu {
    position: absolute; left: 397px; top: 113px; width: 406px; height: 973px;
    background: var(--board); color: var(--ink);
    font-family: "Crimson Text", Georgia, serif;
  }
  .rod { position: absolute; left: 0; width: 406px; height: 12px; }
  .rod-top { top: 16px; }
  .rod-bottom { top: 943px; }
  .brand {
    position: absolute; left: 0; width: 100%; top: 90px; text-align: center;
    font-family: "Cinzel", Georgia, serif; font-weight: 700; font-size: 34px;
    letter-spacing: 2px; color: var(--accent);
  }
  .section { position: absolute; width: 150px; }
  .col-left { left: 27px; }
  .col-right { left: 229px; }
  .section-title {
    height: 27px; line-height: 25px; text-align: center;
    border-top: 2px solid var(--accent); border-bottom: 1px solid var(--accent);
    font-family: "Cinzel", Georgia, serif; font-weight: 600; font-size: 15px; letter-spacing: 0.5px;
  }
  .section-title.light { border-bottom-color: var(--rule); }
  .items { list-style: none; padding-top: 13px; }
  .item { position: relative; height: 28.7px; text-align: center; }
  .item-name { font-weight: 700; font-size: 10px; line-height: 12px; display: block; }
  .item-desc { display: block; font-size: 4.8px; line-height: 5.6px; color: var(--ink-soft); padding: 0 22px; }
  .item-price { position: absolute; right: 4px; top: 1px; font-size: 7px; font-weight: 600; color: var(--ink); }
  .crusts .item { height: 29.3px; }
  .dips { left: 33px; width: 151px; }
  .dip-grid { display: grid; grid-template-columns: 1fr 1fr; row-gap: 17px; padding-top: 19px; }
  .dip { position: relative; text-align: left; padding-left: 4px; font-size: 8.5px; font-weight: 700; }
  .dip .item-price { right: 8px; }
  .soup-name { font-size: 8.5px; }
</style>
</head>
<body>
<main class="menu">
  <svg class="rod rod-top" viewBox="0 0 406 12" aria-hidden="true">
    <line x1="59" y1="6" x2="347" y2="6" stroke="#c4555e" stroke-width="2"/>
    <rect x="133" y="3" width="139" height="6" rx="3" fill="#c4555e"/>
    <circle cx="59" cy="6" r="4" fill="#c4555e"/>
    <circle cx="347" cy="6" r="4" fill="#c4555e"/>
  </svg>

  <h1 class="brand">Valdarossi’s</h1>

  <section class="section col-left" style="top:232px">
    <h2 class="section-title">Pizzas</h2>
    <ul class="items">
      <li class="item"><span class="item-name">Margherita</span><span class="item-price">14</span><span class="item-desc">fresh mozzarella, basil, tomato sauce and olive oil</span></li>
      <li class="item"><span class="item-name">Organic Sausage</span><span class="item-price">16</span><span class="item-desc">fennel sausage, roasted peppers, onion and fresh mozzarella</span></li>
      <li class="item"><span class="item-name">Pepperoni</span><span class="item-price">15</span><span class="item-desc">tomato sauce, pepperoni, mozzarella and oregano</span></li>
      <li class="item"><span class="item-name">Salumi and Burrata</span><span class="item-price">17</span><span class="item-desc">spicy salami, burrata, basil and chili honey</span></li>
      <li class="item"><span class="item-name">Daily Special</span><span class="item-price">17</span></li>
      <li class="item"><span class="item-name">Mushroom</span><span class="item-price">15</span><span class="item-desc">roasted mushrooms, thyme, garlic cream and fontina</span></li>
      <li class="item"><span class="item-name">Prosciutto and Egg</span><span class="item-price">16</span><span class="item-desc">prosciutto, farm egg, arugula, parmesan and lemon oil</span></li>
      <li class="item"><span class="item-name">Quattro Formaggi</span><span class="item-price">15</span><span class="item-desc">four cheeses, honey, black pepper and fresh herbs</span></li>
      <li class="item"><span class="item-name">Farmers Pizza</span><span class="item-price">17</span><span class="item-desc">seasonal vegetables, ricotta, pesto and mozzarella</span></li>
      <li class="item"><span class="item-name">Keto Friendly</span><span class="item-price">17</span><span class="item-desc">cauliflower crust, spinach, mozzarella and tomato</span></li>
    </ul>
  </section>

  <section class="section col-left" style="top:583px">
    <h2 class="section-title">Appetizers</h2>
    <ul class="items">
      <li class="item"><span class="item-name">Brussels</span><span class="item-price">10</span><span class="item-desc">crispy brussels sprouts, balsamic glaze and parmesan</span></li>
      <li class="item"><span class="item-name">Meatballs</span><span class="item-price">12</span><span class="item-desc">mom's recipe, tomato sauce and ricotta</span></li>
      <li class="item"><span class="item-name">Mussels</span><span class="item-price">13</span><span class="item-desc">white wine, garlic and toasted bread</span></li>
      <li class="item"><span class="item-name">Romanesco</span><span class="item-price">11</span><span class="item-desc">roasted romanesco, lemon and chili</span></li>
      <li class="item"><span class="item-name">Chicken wings</span><span class="item-price">10</span><span class="item-desc">wood fired wings with herb dip</span></li>
      <li class="item"><span class="item-name">Burrata</span><span class="item-price">13</span><span class="item-desc">local burrata, tomatoes and handmade bread</span></li>
    </ul>
  </section>

  <section class="section dips" style="top:812px">
    <h2 class="section-title">Dips</h2>
    <div class="dip-grid">
      <div class="dip">Ranch<span class="item-price">1</span></div>
      <div class="dip">Spicy Dip<span class="item-price">1</span></div>
      <div class="dip">Tomato Sauce<span class="item-price">1</span></div>
      <div class="dip">Blue Cheese<span class="item-price">1</span></div>
    </div>
  </section>

  <section class="section col-right" style="top:232px">
    <h2 class="section-title light">Salads</h2>
    <ul class="items">
      <li class="item"><span class="item-name">Chopped Salad</span><span class="item-price">13</span><span class="item-desc">romaine, salami, chickpeas, provolone and oregano dressing</span></li>
      <li class="item"><span class="item-name">Caesar Salad</span><span class="item-price">11</span><span class="item-desc">little gem, parmesan, croutons and anchovy dressing</span></li>
      <li class="item"><span class="item-name">Farm Salad</span><span class="item-price">13</span><span class="item-desc">seasonal greens and vinaigrette</span></li>
      <li class="item"><span class="item-name">Grilled Little Gem</span><span class="item-price">11</span><span class="item-desc">grilled gem, bacon, blue cheese and herbs</span></li>
      <li class="item"><span class="item-name">Spinach and Arugula Salad</span><span class="item-price">13</span><span class="item-desc">spinach, arugula, pear, walnuts and goat cheese</span></li>
    </ul>
  </section>

  <section class="section col-right" style="top:443px">
    <h2 class="section-title light">Sandwiches</h2>
    <ul class="items">
      <li class="item"><span class="item-name">Italian Sub</span><span class="item-price">13</span><span class="item-desc">salami, ham, provolone, peppers and italian dressing</span></li>
      <li class="item"><span class="item-name">Turkey Sandwich</span><span class="item-price">12</span><span class="item-desc">roast turkey, avocado, tomato and aioli</span></li>
      <li class="item"><span class="item-name">Meatball Sub</span><span class="item-price">13</span><span class="item-desc">meatballs, tomato sauce and melted mozzarella</span></li>
      <li class="item"><span class="item-name">Harvest Burger</span><span class="item-price">14</span><span class="item-desc">plant patty, cheddar, pickles and special sauce</span></li>
      <li class="item"><span class="item-name">Chicken Sandwich</span><span class="item-price">13</span><span class="item-desc">crispy chicken, slaw, pickles and spicy mayo</span></li>
    </ul>
  </section>

  <section class="section col-right crusts" style="top:653px">
    <h2 class="section-title">Crusts</h2>
    <ul class="items">
      <li class="item"><span class="item-name">Traditional</span><span class="item-desc">hand crafted dough</span></li>
      <li class="item"><span class="item-name">Gluten Free</span><span class="item-price">3</span><span class="item-desc">made with gluten free flour</span></li>
      <li class="item"><span class="item-name">Cauliflower</span><span class="item-price">3</span><span class="item-desc">light and crisp</span></li>
    </ul>
  </section>

  <section class="section col-right" style="top:796px">
    <h2 class="section-title">Daily Soup</h2>
    <ul class="items">
      <li class="item"><span class="item-name soup-name">Example Tomato Bisque</span><span class="item-price">8</span></li>
    </ul>
  </section>

  <svg class="rod rod-bottom" viewBox="0 0 406 12" aria-hidden="true">
    <line x1="59" y1="6" x2="347" y2="6" stroke="#c4555e" stroke-width="2"/>
    <rect x="133" y="3" width="139" height="6" rx="3" fill="#c4555e"/>
    <circle cx="59" cy="6" r="4" fill="#c4555e"/>
    <circle cx="347" cy="6" r="4" fill="#c4555e"/>
  </svg>
</main>
</body>
</html>
```